Cover for elementary school yearbook.

Need is for a book cover for an elementary yearbook school. The theme of the book is "Building A Cardinal Legacy". The school is under renovation after 30 years of use. We are looking for a front and back cover that equals 17x11 total folded in half. The theme of the book, "Fox Hollow Elementary"and "2016-2017" must be displayed on the "front" of the cover. The scholl masicot is the cardinal and color is red. The new floor plan of the school is attached. We were thinking of a design that has visual elements associated with blue prints.

Target Market(s)

Elementary children and parents.

Industry/Entity Type

School

Font styles to use
Serif
Sans Serif

Colors
ec1f27
0456a4

Requirements
Must have
• Name of school, yearbook theme, and years.
• Also - the final size must be under 50MB. The following file types can be used: .jpeg, .eps, .psd, .ai, or .tiff. Acceptable software files include Adobe Photoshop (v 4.0 and higher), Illustrator ( v 6.0 and higher), InDesign (all versions). Regarding resolution - line art should be 500 DPI, grayscale should be 225 DPI, and color should be 300 DPI.
Nice to have
• We like the idea of blue prints and construction.
Should not have
• Mature artwork. Should not look like a corporate product.

```html
<!DOCTYPE html>
<html lang="en">
<head>
<meta charset="utf-8">
<title>Fox Hollow Elementary Yearbook Cover 2016-2017</title>
<link rel="stylesheet" href="https://fonts.googleapis.com/css2?family=PT+Sans:wght@400;700&family=Caveat+Brush&display=swap">
<style>
  :root {
    --paper-light: #e4e4e4;
    --paper-mid: #d3d3d3;
    --paper-dark: #c6c6c6;
    --maroon: #8e1b2e;
    --cardinal-red: #ec1f27;
    --tile-red: #e01f26;
    --tile-blue: #0b4fa3;
    --tile-yellow: #d8dc4c;
    --band-black: #111111;
    --theme-blue: #0456a4;
  }
  html, body {
    margin: 0;
    padding: 0;
    width: 1200px;
    height: 789px;
    overflow: hidden;
    background: var(--paper-mid);
  }
  .cover {
    position: relative;
    width: 1200px;
    height: 789px;
    overflow: hidden;
  }
  .cover-art {
    display: block;
    width: 1200px;
    height: 789px;
  }
  .school-name {
    font-family: "PT Sans", sans-serif;
    font-weight: 400;
    font-size: 33px;
    letter-spacing: 1.5px;
    fill: var(--maroon);
  }
  .theme-lead {
    font-family: "PT Sans", sans-serif;
    font-weight: 400;
    font-size: 44px;
    letter-spacing: 9px;
    fill: var(--theme-blue);
  }
  .theme-main {
    font-family: "Caveat Brush", cursive;
    font-size: 96px;
    fill: var(--cardinal-red);
  }
  .school-year {
    font-family: "PT Sans", sans-serif;
    font-weight: 400;
    font-size: 29px;
    letter-spacing: 1px;
    fill: var(--cardinal-red);
  }
  .rule { stroke: var(--theme-blue); stroke-width: 3; stroke-linecap: round; }
  .tile-red { fill: var(--tile-red); }
  .tile-blue { fill: var(--tile-blue); }
  .tile-yellow { fill: var(--tile-yellow); }
</style>
</head>
<body>
<main class="cover">
  <svg class="cover-art" viewBox="0 0 1200 789" xmlns="http://www.w3.org/2000/svg">
    <defs>
      <linearGradient id="paper" x1="0" y1="0" x2="1" y2="1">
        <stop offset="0" stop-color="#d6d6d6"/>
        <stop offset="0.5" stop-color="#e2e2e2"/>
        <stop offset="1" stop-color="#cfcfcf"/>
      </linearGradient>
      <linearGradient id="photo-lecture" x1="0" y1="0" x2="0" y2="1">
        <stop offset="0" stop-color="#3a4a7a"/><stop offset="1" stop-color="#9c7f78"/>
      </linearGradient>
      <linearGradient id="photo-playground" x1="0" y1="0" x2="0" y2="1">
        <stop offset="0" stop-color="#6f6d4c"/><stop offset="1" stop-color="#8d8a78"/>
      </linearGradient>
      <linearGradient id="photo-classroom" x1="0" y1="0" x2="0" y2="1">
        <stop offset="0" stop-color="#8a4a3e"/><stop offset="1" stop-color="#b53a3a"/>
      </linearGradient>
      <linearGradient id="photo-reading" x1="0" y1="0" x2="1" y2="0">
        <stop offset="0" stop-color="#6a4a36"/><stop offset="1" stop-color="#7c8aa0"/>
      </linearGradient>
      <linearGradient id="photo-friends" x1="0" y1="0" x2="1" y2="0">
        <stop offset="0" stop-color="#7a6454"/><stop offset="1" stop-color="#5a4a3e"/>
      </linearGradient>
      <linearGradient id="photo-play" x1="0" y1="0" x2="0" y2="1">
        <stop offset="0" stop-color="#3f6f9a"/><stop offset="1" stop-color="#1a1a2a"/>
      </linearGradient>
      <linearGradient id="photo-group" x1="0" y1="0" x2="0" y2="1">
        <stop offset="0" stop-color="#7a7a76"/><stop offset="1" stop-color="#3e4660"/>
      </linearGradient>
      <linearGradient id="photo-mascot" x1="0" y1="0" x2="0" y2="1">
        <stop offset="0" stop-color="#a7a9ad"/><stop offset="1" stop-color="#8c6d62"/>
      </linearGradient>
    </defs>

    <rect class="floor-plan" x="0" y="0" width="1200" height="789" fill="url(#paper)"
          role="img" aria-label="Faint pencil floor plan of the school on grey wood-grain paper"/>

    <g class="masthead">
      <text class="school-name" x="1060" y="88" text-anchor="end">FOX HOLLOW ELEMENTARY</text>
      <circle class="school-mark" cx="1122" cy="76" r="28" fill="var(--maroon)"/>
    </g>

    <g class="photo-band" transform="translate(-20 470) rotate(-9.5)">
      <rect x="0" y="-4" width="1290" height="268" fill="var(--band-black)"/>

      <rect class="tile-yellow" x="0" y="0" width="78" height="128"/>
      <rect x="82" y="0" width="190" height="128" fill="url(#photo-lecture)" role="img" aria-label="Photo: children raising hands at an assembly"/>
      <rect x="276" y="0" width="190" height="128" fill="url(#photo-playground)" role="img" aria-label="Photo: children on a playground spinner"/>
      <rect class="tile-red" x="470" y="0" width="196" height="128"/>
      <rect x="670" y="0" width="196" height="128" fill="url(#photo-classroom)" role="img" aria-label="Photo: class in red shirts around a painted mural"/>
      <rect class="tile-blue" x="870" y="0" width="200" height="128"/>
      <rect x="1074" y="0" width="190" height="128" fill="url(#photo-reading)" role="img" aria-label="Photo: teacher with two students in a reading corner"/>
      <rect class="tile-blue" x="1268" y="0" width="22" height="128"/>

      <rect x="0" y="132" width="212" height="128" fill="url(#photo-friends)" role="img" aria-label="Photo: two smiling girls outdoors"/>
      <rect class="tile-blue" x="216" y="132" width="196" height="128"/>
      <rect x="416" y="132" width="196" height="128" fill="url(#photo-play)" role="img" aria-label="Photo: children in pilgrim costumes at a school play"/>
      <rect class="tile-yellow" x="616" y="132" width="196" height="128"/>
      <rect x="816" y="132" width="196" height="128" fill="url(#photo-group)" role="img" aria-label="Photo: students and staff posing in a group"/>
      <rect x="1016" y="132" width="196" height="128" fill="url(#photo-mascot)" role="img" aria-label="Photo: cardinal mascot costume lounging on a bench"/>
      <rect class="tile-red" x="1216" y="132" width="74" height="128"/>
    </g>

    <g class="theme-lead-group" transform="translate(744 658) rotate(-11)">
      <line class="rule" x1="-105" y1="-10" x2="-20" y2="-10"/>
      <text class="theme-lead" x="0" y="0">BUILDING A</text>
      <line class="rule" x1="322" y1="-10" x2="410" y2="-10"/>
    </g>

    <g class="theme-main-group" transform="translate(645 738) rotate(-9.5)">
      <text class="theme-main" x="0" y="0" textLength="525" lengthAdjust="spacingAndGlyphs">Cardinal Legacy</text>
    </g>

    <text class="school-year" x="1168" y="746" text-anchor="end">2016-2017</text>
  </svg>
</main>
</body>
</html>
```